Professional Services Business Card Design

We need a business card design for a relatively new (less than one year old) company. Tidewell Advisory Partners, LLC provides professional support services and expert assistance in acquisition management to federal agencies, and also provides acquisition workforce personnel training and development for defense and civilian agencies. The colors used should incorporate the colors found within the company's logo, which is attached.

Font styles to use
Serif
Sans Serif

```html
<!DOCTYPE html>
<html lang="en">
<head>
<meta charset="utf-8">
<title>Tidewell Advisory Partners – Business Card</title>
<link href="https://fonts.googleapis.com/css2?family=Roboto:wght@400;700&display=swap" rel="stylesheet">
<style>
  :root {
    --navy: #262e50;
    --grey: #8a8e9c;
    --text-grey: #6f7280;
    --white: #ffffff;
    --backdrop: #d8dade;
  }
  html, body {
    margin: 0;
    width: 1200px;
    height: 1000px;
    overflow: hidden;
    background: var(--backdrop);
  }
  .card {
    position: absolute;
    left: 302px;
    width: 595px;
    height: 340px;
    border-radius: 18px;
    box-shadow: 0 10px 28px rgba(20, 24, 40, 0.25);
    overflow: hidden;
  }
  .card--back { top: 110px; background: var(--navy); }
  .card--front { top: 530px; background: var(--white); }

  .brand {
    position: absolute;
    display: flex;
    align-items: center;
    gap: 12px;
    font-family: "Roboto", sans-serif;
    font-weight: 400;
    white-space: nowrap;
  }
  .brand__dot { flex: none; border-radius: 50%; }
  .brand__name { margin: 0; }

  .card--back .brand { color: var(--white); left: 50%; top: 50%; transform: translate(-50%, -50%); }
  .card--back .brand__dot { width: 22px; height: 22px; background: var(--white); }
  .card--back .brand__name { font-size: 26px; }

  .card--front .brand { color: var(--navy); right: 34px; top: 40px; gap: 10px; }
  .card--front .brand__dot { width: 14px; height: 14px; background: var(--navy); }
  .card--front .brand__name { font-size: 17px; }

  .person { position: absolute; left: 0; top: 96px; font-family: "Roboto", sans-serif; }
  .person__bar { position: absolute; left: 0; top: 0; width: 8px; height: 52px; background: var(--navy); }
  .person__name { position: absolute; left: 26px; top: 0; margin: 0; font-size: 26px; font-weight: 700; color: var(--navy); white-space: nowrap; letter-spacing: 0.02em; }
  .person__title { position: absolute; left: 24px; top: 34px; margin: 0; font-size: 17px; color: var(--text-grey); white-space: nowrap; }
  .divider { position: absolute; left: 180px; top: 145px; width: 360px; height: 1.5px; background: var(--navy); }

  .address {
    position: absolute; left: 26px; top: 172px; margin: 0;
    font-family: "Roboto", sans-serif; font-style: normal; font-size: 15px; line-height: 1.35; color: var(--grey);
  }

  .contacts {
    position: absolute; right: 26px; bottom: 24px; margin: 0; padding: 0; list-style: none;
    font-family: "Roboto", sans-serif; font-size: 15px; color: var(--text-grey);
  }
  .contacts li { display: flex; justify-content: flex-end; align-items: center; gap: 10px; height: 24px; }
  .contacts svg { width: 14px; height: 14px; fill: none; stroke: var(--navy); stroke-width: 2; }
</style>
</head>
<body>

<section class="card card--back" aria-label="Card back">
  <div class="brand">
    <span class="brand__dot"></span>
    <p class="brand__name">Tidewell Advisory Partners, LLC</p>
  </div>
</section>

<section class="card card--front" aria-label="Card front">
  <div class="brand">
    <span class="brand__dot"></span>
    <p class="brand__name">Tidewell Advisory Partners, LLC</p>
  </div>

  <div class="person">
    <span class="person__bar"></span>
    <h1 class="person__name">Marcus Hale</h1>
    <p class="person__title">General Manager</p>
  </div>
  <div class="divider"></div>

  <address class="address">Harbor Point Plaza, Suite 4<br>Annapolis, 21401</address>

  <ul class="contacts">
    <li>03 5550 2741
      <svg viewBox="0 0 24 24"><path d="M5 3h4l2 5-3 2a12 12 0 0 0 6 6l2-3 5 2v4a2 2 0 0 1-2 2A17 17 0 0 1 3 5a2 2 0 0 1 2-2z"/></svg></li>
    <li>0455 019 382
      <svg viewBox="0 0 24 24"><rect x="6" y="2" width="12" height="20" rx="2"/><line x1="11" y1="18" x2="13" y2="18"/></svg></li>
    <li>hello@tidewelladvisory.com
      <svg viewBox="0 0 24 24"><rect x="3" y="5" width="18" height="14" rx="1"/><path d="M3 6l9 7 9-7"/></svg></li>
    <li>www.tidewelladvisory.com
      <svg viewBox="0 0 24 24"><circle cx="12" cy="12" r="9"/><path d="M3 12h18M12 3a14 14 0 0 1 0 18M12 3a14 14 0 0 0 0 18"/></svg></li>
  </ul>
</section>

</body>
</html>
```